Advertising agency needs site design

You will be designing a clean (plenty of white space) and vivid (colorful) design that is for an advertising agency named Brightwell Reach. Their current web site is located at www.BrightwellReach.net. From there you can see their services and get a feel for the company as the site stands today.
The following are direct quotes from the client:
“I want a clean look with colors of the teal blue, deep yellow (in logo) and then a good energetic orange (deep orange - rich) should bring a good feel and enthusiasm.”
“The orange can be a nice accent color, not dominant.”
“Saw two other things I like - the website lanternkitestudio.com was pretty cool. I liked how the top banner changed colors as you moved to different tabs. I am somewhat wanting the colors I mentioned - like the blue color we use can be lighter as long as it works with the logo. - love the tulip forge site. I want quirky, creative and clean look - fun feel but slightly sophisticated to work with the medical field.”
Brightwell Reach currently focuses on the following primary industries:
• Medical / Health Care – Currently the primary industry
• Retail Industry
• Automotive Industry
• Entertainment Industry
Primary Services
• Media Planning & Buying: Web, TV, Print, Radio
• Campaign monitoring and reporting
• Commercial Production: TV & Radio
• Strategic Planning
• Market Research
• Internet Marketing: Email, SEO, Web design / development
Primary Navigation will consist of the following:
• Home
• About Us
o History
o Principal Profile (sub nav)
o Sales Team & Partners
• Clients
• Services
• Testimonials
• Contact Us
They want the web site to act as a basis for future marketing collateral so the overall feel from the web site must be capable of translating to print and other collateral. I do not currently have a clean digital version of their logo however their logo is on the web site (brightwellreach.net)
Reason: Still awaiting feedback from client on designs. They should be back to us shortly.
Target Market(s)
larger companies that are purchasing air time on television and radio. Typically in the health care industry and others described above in brief.
Industry/Entity Type
Advertising
Look and feel
Each slider illustrates characteristics of the customer's brand and the style your logo design should communicate.

```html
<!DOCTYPE html>
<html lang="en">
<head>
<meta charset="utf-8">
<title>Brightwell Reach</title>
<link rel="stylesheet" href="https://fonts.googleapis.com/css2?family=Arimo:wght@400;700&display=swap">
<style>
:root{
  --blue-deep:#0a3f97;
  --blue-mid:#1a6fc9;
  --blue-light:#38b6ec;
  --nav-blue:#1596e6;
  --orange:#f7941d;
  --orange-text:#f68b1f;
  --navy-text:#0c3c8c;
  --body-text:#1e1e1e;
  --card-top:#f3f4f5;
  --footer-top:#1d5a93;
  --footer-bottom:#0e3a6a;
  --white:#ffffff;
}
*{margin:0;padding:0;box-sizing:border-box}
html,body{width:1200px;height:1097px;overflow:hidden;background:var(--white)}
body{position:relative;font-family:"Arimo",Arial,sans-serif;color:var(--body-text)}
.abs{position:absolute}
.header{left:0;top:0;width:1200px;height:363px;
  background:linear-gradient(100deg,var(--blue-deep) 0%,var(--blue-mid) 45%,var(--blue-light) 75%,var(--blue-mid) 100%)}
.header::after{content:"";position:absolute;left:0;top:0;width:100%;height:5px;background:var(--blue-light)}
.nav{left:344px;top:0;width:817px;height:47px;border-radius:0 0 10px 10px;
  background:linear-gradient(var(--blue-light),var(--nav-blue));display:flex;padding-left:12px}
.nav a{color:var(--white);text-decoration:none;font-weight:700;font-size:16.5px;line-height:47px;padding:0 10px;white-space:nowrap}
.nav a.active{background:var(--orange);color:var(--blue-deep);font-weight:700}
.brand{left:33px;top:48px;color:var(--white);font-size:44px;font-weight:400;letter-spacing:1px}
.mission{left:35px;top:182px;width:480px;color:var(--white);font-size:20.5px;line-height:27px}
.slider-frame{left:538px;top:108px;width:603px;height:322px;background:var(--white);
  box-shadow:0 4px 14px rgba(0,0,0,.25)}
.slider-art{left:551px;top:121px;width:577px;height:299px;
  background:radial-gradient(ellipse at 45% 40%,#f7b22a 0%,#d85314 30%,#5a1d12 60%,#0b0604 85%)}
.dots{left:548px;top:451px;display:flex;gap:12px}
.dot{width:16px;height:16px;border-radius:50%;background:var(--nav-blue)}
.dot.on{background:var(--orange)}
.portfolio-icon{left:56px;top:374px;width:95px;height:105px;border-radius:6px;
  background:linear-gradient(90deg,#8f1313,#d42a2a 60%,#a01818)}
.portfolio-cta{left:170px;top:402px;color:var(--orange-text)}
.portfolio-cta .small{font-size:21px}
.portfolio-cta .big{font-size:28px;margin-top:2px}
.rule{left:0;top:485px;width:1200px;height:1px;background:#e2e2e2}
.welcome{left:58px;top:505px;width:745px}
.welcome h1{color:var(--navy-text);font-size:30.5px;font-weight:400;margin-bottom:14px}
.welcome p{font-size:14.3px;line-height:20px;text-align:justify;margin-bottom:19px}
.welcome-art{left:857px;top:528px;width:266px;height:197px;
  background:linear-gradient(180deg,#c987e6 0%,#a97fd6 60%,#8fb38c 85%,#6f9b6a 100%)}
.card{top:742px;height:281px;background:linear-gradient(var(--card-top),var(--white) 85%);
  box-shadow:0 0 8px rgba(0,0,0,.08)}
.card .icon{position:absolute;border-radius:8px}
.card h2{position:absolute;font-weight:400;white-space:nowrap}
.card p{position:absolute;font-size:13.4px;line-height:22px;text-align:justify}
.card .more{position:absolute;display:flex;align-items:center;gap:6px;color:var(--nav-blue);font-size:14.5px}
.card-creative{left:33px;width:357px}
.card-internet{left:392px;width:413px}
.card-planning{left:807px;width:356px}
.footer{left:0;top:1035px;width:1200px;height:62px;
  background:linear-gradient(var(--footer-top),var(--footer-bottom));color:var(--white);font-size:14.5px}
.footer span{position:absolute;top:25px}
</style>
</head>
<body>
<div class="abs header"></div>
<nav class="abs nav">
  <a href="#">Home</a><a href="#" class="active">About Us</a><a href="#">History</a><a href="#">Sales Team &amp; Partners</a><a href="#">Clients</a><a href="#">Services</a><a href="#">Testimonials</a><a href="#">Contact Us</a>
</nav>
<div class="abs brand">Brightwell Reach</div>
<p class="abs mission">Our Mission is to Apply our experience, creativity and energy to assemble and excute marketing solutions with maximum impact. Implementation of carefully designer plans is undertaken with strict regards to value and results, always striving to exceed client expectations.</p>

<div class="abs slider-frame"></div>
<div class="abs slider-art" role="img" aria-label="Slideshow image of glowing orange and gold light swirls on black"></div>
<div class="abs dots"><span class="dot on"></span><span class="dot"></span><span class="dot"></span><span class="dot"></span><span class="dot"></span><span class="dot"></span></div>

<div class="abs portfolio-icon" role="img" aria-label="Red spiral-bound portfolio book"></div>
<div class="abs portfolio-cta"><div class="small">Click view to</div><div class="big">Our Portfolio</div></div>
<div class="abs rule"></div>

<section class="abs welcome">
  <h1>Welcome to Brightwell Reach</h1>
  <p>Full service. Dynamic exposure. Negotiation savvy. More buying power. Expert placement. Comprehensive promotional opportunities. And big savings. Simply put, more media impact for your dollar.</p>
  <p>Our long-standing relationships with the media give us stronger buying clout and broader opportunities than many of our competitors. And, we make it our business to stay on top of promotional and cooperative opportunities, passing incredible savings and increased exposure to you!</p>
  <p>Over 20 years in the media and marketing industries positions us to deliver the results our clients depend upon.</p>
</section>
<div class="abs welcome-art" role="img" aria-label="Illustration of an archer aiming at a target over a purple and green money backdrop"></div>

<section class="abs card card-creative">
  <div class="icon" role="img" aria-label="Paint brushes and palette" style="left:12px;top:5px;width:78px;height:88px;background:linear-gradient(135deg,#e6603a,#8f6fd1,#6c9bd8)"></div>
  <h2 style="left:103px;top:29px;color:var(--orange-text);font-size:28px">Creative</h2>
  <h2 style="left:103px;top:63px;color:var(--orange-text);font-size:21px">Development</h2>
  <p style="left:25px;top:112px;width:296px">Our agency can create the concept from start to finish. We have exceptionally creative thinkers that can produce the right campaign ideas for your company. Our campaigns produce results and build brand awareness.</p>
  <div class="more" style="left:218px;top:228px">Read more <svg width="22" height="18" viewBox="0 0 22 18"><path d="M0 5h11V0l11 9-11 9v-5H0z" fill="#2aa6e6"/></svg></div>
</section>

<section class="abs card card-internet">
  <div class="icon" role="img" aria-label="Magnifying glass over a globe" style="left:26px;top:28px;width:74px;height:74px;border-radius:50%;background:radial-gradient(circle,#4fa3e0,#2a7a3c 70%,#1b3f7a)"></div>
  <h2 style="left:110px;top:34px;color:var(--navy-text);font-size:25px">Internet Marketing</h2>
  <h2 style="left:110px;top:64px;color:var(--navy-text);font-size:21px">Search Engine Optimization</h2>
  <p style="left:26px;top:113px;width:360px">Internet marketing is highly effective. Currently only a small amount of businesses are using internet marketing. Mainly because they are not familiar with HOW to implement it. Postioning your company to appear on the 1st page of a search is the key.</p>
  <div class="more" style="left:278px;top:221px">Read more <svg width="22" height="18" viewBox="0 0 22 18"><path d="M0 5h11V0l11 9-11 9v-5H0z" fill="#2aa6e6"/></svg></div>
</section>

<section class="abs card card-planning">
  <svg class="icon" style="left:28px;top:38px" width="58" height="42" viewBox="0 0 58 42" aria-hidden="true">
    <g fill="none" stroke="#123e8f" stroke-width="6">
      <path d="M0 9h14c10 0 16 24 26 24h6"/><path d="M0 33h14c10 0 16-24 26-24h6"/>
    </g>
    <path d="M44 0l14 9-14 9zM44 24l14 9-14 9z" fill="#123e8f"/>
  </svg>
  <h2 style="left:106px;top:44px;color:var(--orange-text);font-size:26px">Media Planning</h2>
  <p style="left:29px;top:91px;width:300px">Brightwell Reach will develop a comprehensive, customized media plan that best utilizes the mediums most beneficial to your business goals. We use a fully computerized planning system, PlanWise, that is the most innovative software available today.</p>
  <div class="more" style="left:235px;top:221px">Read more <svg width="22" height="18" viewBox="0 0 22 18"><path d="M0 5h11V0l11 9-11 9v-5H0z" fill="#2aa6e6"/></svg></div>
</section>

<footer class="abs footer">
  <span style="left:34px">Copyright Text</span>
  <span style="right:40px">Site Developed by Copperleaf Creative, LLC</span>
</footer>
</body>
</html>
```